Design ecommerce website for www.velmorissa.com

Design a Website given below details
Name - www.velmorissa.com

Given a shopify theme :Brightcart
http://layoutbazaar.net/item/brightcart-responsive-shopify-theme/4817203

Given type of products that will be sold
http://tarokbars.pelisite.com
Wendlomart.in
( above designs are not good )

Given competitors
www.zorbelle.com ( especially like how each category is sold as a story )
www.gindova.com

Given Tg
Women 20 +
Aspirational

Website has to be fresh peppy and understated sexy

No need to push Organic agenda too much but it is present in background story

Let me know if any more info required
Updates

Reason: Look for forward to revised designs / new designs

Target Market(s)

Women
20 +
Primarily Indian
Aspirational

Industry/Entity Type

Hair And Beauty

Number of Pages Required

5+ page

Font styles to use
Sans Serif

Requirements
Must have
• Hi Quality Images ( i will provide images )
• Good fun icons
• Good font
• Peppy / classy color scheme
• THe main focus is on the main page / landing page. Need a design which is intuitive and lends itself well to beauty products. Creating an exclusive experiance for women
• The other pages are
• Modified page for product categories ( eg page for all Skin products )
• Modified page for each product
• About page / Check out page
• These are essentially modifications to main page with minor alterations
• Important to remember that we are building using the Brightcart Shopify theme.
• If you recommend shopify apps, I would purchase those too.
Nice to have
• Disctintive fonts.
• Usage of elements/ fonts / icons which make the site very quirky and fun
• I am open to suggestions to changes in words or using images instead of words to convey information
Should not have
• Too much of green / organic feel
• Too much artificial feel ( no neons )

```html
<!DOCTYPE html>
<html lang="en">
<head>
<meta charset="utf-8">
<title>Velmorissa – Home</title>
<link rel="stylesheet" href="https://fonts.googleapis.com/css2?family=Oswald:wght@300;400;500&family=Open+Sans:wght@400;600;700&family=Merriweather:wght@400;700&display=swap">
<style>
:root{
  --green:#7cc242;
  --green-dark:#5fa32c;
  --green-pale:#e6f3d8;
  --ink:#2c2c2c;
  --charcoal:#333333;
  --charcoal-deep:#222222;
  --grey-bg:#f0f0f0;
  --grey-line:#d8d8d8;
  --text:#555555;
  --white:#ffffff;
  --star:#f4a623;
  --stamp:#d9262b;
}
*{box-sizing:border-box;margin:0;padding:0}
html,body{width:1200px;height:3180px;overflow:hidden}
body{font-family:"Open Sans",Arial,sans-serif;color:var(--text);background:var(--white);position:relative}
.abs{position:absolute}
.photo{position:absolute}
.btn{position:absolute;display:flex;align-items:center;justify-content:center;gap:8px;background:var(--green);color:var(--white);font-family:"Open Sans",Arial,sans-serif;font-weight:700;border-radius:4px}
.cond{font-family:"Oswald",Arial,sans-serif;text-transform:uppercase}

/* promo strip */
.promo{position:absolute;left:0;top:0;width:1200px;height:132px;background:linear-gradient(90deg,#eaf6f4,#ffffff 45%,#eef7f2)}
.promo-title{left:360px;top:14px;font-family:"Merriweather",Georgia,serif;font-size:44px;font-weight:700;color:var(--green)}
.promo-sub{left:362px;top:72px;font-family:"Merriweather",Georgia,serif;font-size:34px;color:var(--ink)}
.promo .btn{left:890px;top:18px;width:150px;height:46px;border-radius:23px;font-size:18px}

/* utility bar */
.utility{position:absolute;left:560px;top:132px;width:640px;height:36px;background:var(--charcoal);display:flex;align-items:center;gap:26px;padding-left:30px;font-size:13px;color:var(--white)}
.utility .item{display:flex;align-items:center;gap:6px}
.utility .search{margin-left:auto;margin-right:12px;width:170px;height:24px;background:var(--white);color:#888;font-size:12px;padding:3px 8px}

/* header */
.header{position:absolute;left:0;top:168px;width:1200px;height:152px;background:var(--white)}
.logo{position:absolute;left:76px;top:56px;width:266px;height:90px;border:2px solid var(--green);display:flex;align-items:center;justify-content:center;gap:12px;font-size:38px;font-weight:600;color:var(--green)}
.logo .dot{width:22px;height:22px;border-radius:50%;background:var(--green)}
.nav{position:absolute;left:520px;top:62px;display:flex;align-items:center;gap:38px;font-size:17px;color:var(--ink)}
.nav .active{background:var(--green);color:var(--white);padding:8px 22px;border-radius:3px}
.nav .offer{color:var(--green)}

/* hero */
.hero{position:absolute;left:0;top:320px;width:1200px;height:472px;background:linear-gradient(90deg,#c9a48e 0%,#e9ddd4 30%,#f1ede9 55%,#d9c8bd 75%,#b58b7a 100%)}
.hero-circle{position:absolute;left:410px;top:50px;width:360px;height:360px;border-radius:50%;background:var(--white);border:10px solid var(--green);display:flex;flex-direction:column;align-items:center;justify-content:center;text-align:center}
.hero-circle h2{font-family:"Oswald",Arial,sans-serif;font-weight:400;font-size:26px;line-height:1.3;color:var(--ink);text-transform:uppercase;width:260px}
.hero-circle .btn{position:static;margin-top:22px;width:150px;height:44px;font-size:17px}
.dots{position:absolute;left:490px;top:430px;display:flex;gap:16px}
.dots span{width:18px;height:18px;border-radius:50%;border:2px solid var(--ink);background:var(--white)}
.dots span.on{background:var(--ink)}

/* dark band */
.season{position:absolute;left:0;top:792px;width:1200px;height:256px;background:linear-gradient(180deg,#3a3a3a,#262626)}
.season h2{position:absolute;left:250px;top:60px;width:700px;text-align:center;font-family:"Oswald",Arial,sans-serif;font-weight:300;font-size:36px;line-height:1.3;color:var(--white);text-transform:uppercase}
.season .btn{left:530px;top:178px;width:140px;height:44px;font-size:17px}

/* tiles */
.tile{position:absolute;top:1100px;width:312px;height:280px;overflow:hidden}
.tile-label{position:absolute;font-family:"Oswald",Arial,sans-serif;text-transform:uppercase;color:var(--white);font-size:32px;line-height:1.15}
.tile .dark-btn{position:absolute;left:40px;bottom:28px;width:170px;height:38px;background:var(--charcoal);color:var(--white);font-size:14px;font-weight:700;display:flex;align-items:center;justify-content:center}

/* recipe banner */
.recipe{position:absolute;left:0;top:1400px;width:1200px;height:208px;background:linear-gradient(90deg,#d8ecc4,#f5faef 50%,#d8ecc4)}
.recipe-card{position:absolute;left:420px;top:28px;width:420px;height:152px;background:rgba(255,255,255,.85);display:flex;flex-direction:column;align-items:center;justify-content:center}
.recipe-card h2{font-family:"Oswald",Arial,sans-serif;font-weight:400;font-size:30px;color:var(--green);text-transform:uppercase;text-align:center;line-height:1.2}
.recipe-card .btn{position:static;margin-top:14px;width:130px;height:40px;font-size:17px}

/* two panels */
.panel{position:absolute;top:1632px;height:388px;background:var(--grey-bg)}
.panel h2{position:absolute;font-family:"Oswald",Arial,sans-serif;font-weight:400;font-size:34px;line-height:1.2;color:var(--green-dark);text-transform:uppercase}
.panel p{position:absolute;font-size:13px;line-height:1.6;color:var(--text)}

/* products */
.section-title{position:absolute;left:0;width:1200px;text-align:center;font-family:"Oswald",Arial,sans-serif;font-weight:400;font-size:34px;color:var(--green);text-transform:uppercase}
.title-rule{position:absolute;left:520px;width:160px;height:12px}
.card{position:absolute;top:2180px;width:228px;height:300px;background:var(--white);border:1px solid var(--grey-line)}
.card .img{position:absolute;left:14px;top:14px;width:198px;height:150px}
.card .name{position:absolute;left:0;top:178px;width:226px;text-align:center;font-size:12px;font-weight:700;color:var(--green)}
.card .stars{position:absolute;left:0;top:198px;width:226px;text-align:center;font-size:16px;color:var(--star);letter-spacing:2px}
.card .stars i{font-style:normal;color:#ccc}
.card .price{position:absolute;left:0;top:226px;width:226px;text-align:center;font-size:17px;color:var(--ink)}
.card .actions{position:absolute;left:0;bottom:0;width:226px;height:34px;border-top:1px solid var(--grey-line);display:flex;align-items:center;justify-content:center;gap:12px;font-size:11px;color:var(--ink)}

/* testimonial */
.testimonial{position:absolute;left:0;top:2560px;width:1200px;height:400px;background:linear-gradient(180deg,#efefef,#e3e3e3)}
.quote{position:absolute;left:280px;top:170px;width:640px;text-align:center;font-size:15px;line-height:1.7;color:var(--text)}
.client{position:absolute;left:0;top:302px;width:1200px;text-align:center;font-size:15px;color:var(--green);font-weight:600}

/* footer */
.footer{position:absolute;left:0;top:2960px;width:1200px;height:160px;background:var(--charcoal);color:var(--white)}
.footer .care{position:absolute;left:76px;top:50px;display:flex;gap:14px;align-items:center;font-size:14px;line-height:1.6}
.footer .news{position:absolute;left:470px;top:40px;font-size:14px}
.footer .news .field{margin-top:10px;width:260px;height:32px;background:var(--white);color:#888;font-size:12px;padding:7px 10px}
.footer .connect{position:absolute;left:856px;top:36px;font-size:14px}
.footer .social{display:flex;gap:14px;margin-top:12px}
.footer .social span{width:42px;height:42px;border-radius:50%;background:#4a4a4a;border:2px solid #666}
.footer .social span:first-child{background:var(--green);border-color:var(--green)}
.legal{position:absolute;left:0;top:3120px;width:1200px;height:60px;background:var(--charcoal-deep);font-size:13px;color:#bbb}
.legal .links{position:absolute;left:0;top:8px;width:1200px;display:flex;justify-content:center;gap:90px;text-transform:uppercase;font-size:12px}
.legal .links span:first-child{color:var(--green)}
.legal .copy{position:absolute;left:0;top:36px;width:1200px;text-align:center;font-size:12px}
</style>
</head>
<body>

<!-- promo strip -->
<section class="promo">
  <div class="photo" role="img" aria-label="Beauty product jars and tubes" style="left:150px;top:10px;width:190px;height:112px;background:linear-gradient(135deg,#bfe0d6,#8fc7b5)"></div>
  <div class="abs promo-title">Natural Product</div>
  <div class="abs promo-sub">Up to 15% off</div>
  <div class="photo" role="img" aria-label="Cosmetic products and soap bars" style="left:740px;top:70px;width:330px;height:60px;background:linear-gradient(90deg,#a9d7a0,#e9f1e4)"></div>
  <div class="photo" role="img" aria-label="Green cosmetic jars" style="left:1060px;top:10px;width:120px;height:112px;background:linear-gradient(135deg,#9fd39a,#dff0da)"></div>
  <div class="btn">SHOP NOW</div>
</section>

<!-- utility bar -->
<div class="utility">
  <span class="item"><svg width="12" height="12" viewBox="0 0 12 12"><circle cx="6" cy="4" r="3" fill="#7cc242"/><path d="M0 12a6 5 0 0 1 12 0z" fill="#7cc242"/></svg>Account</span>
  <span class="item"><svg width="14" height="10" viewBox="0 0 14 10"><rect x=".5" y=".5" width="13" height="9" fill="none" stroke="#fff"/><path d="M.5 .5l6.5 5 6.5-5" fill="none" stroke="#fff"/></svg>Contact us</span>
  <span class="item"><svg width="14" height="12" viewBox="0 0 14 12"><path d="M0 1h3l2 7h7l2-5H4" fill="none" stroke="#fff" stroke-width="1.4"/><circle cx="6" cy="11" r="1" fill="#fff"/><circle cx="11" cy="11" r="1" fill="#fff"/></svg>My Cart</span>
  <span class="search">Search Here...</span>
</div>

<!-- header -->
<header class="header">
  <div class="logo"><span class="dot"></span>Velmorissa</div>
  <nav class="nav">
    <span class="active">Skin</span>
    <span>Hair</span>
    <span>Make Up</span>
    <span>Bath and Body</span>
    <span class="offer">Offer zone</span>
  </nav>
</header>

<!-- hero -->
<section class="hero" role="img" aria-label="Woman with glossy hair beside an arrangement of skincare and makeup products">
  <div class="hero-circle">
    <h2>Look for customised offers and recommendations</h2>
    <span class="btn">Shop Now</span>
  </div>
  <div class="dots"><span class="on"></span><span></span><span></span><span></span><span></span><span></span></div>
</section>

<!-- season band -->
<section class="season">
  <div class="photo" role="img" aria-label="Row of red and pink lipsticks" style="left:0;top:0;width:300px;height:256px;background:linear-gradient(90deg,#5a2a30,#3a3a3a)"></div>
  <div class="photo" role="img" aria-label="Woman applying lipstick next to a foundation bottle" style="left:880px;top:0;width:320px;height:256px;background:linear-gradient(90deg,#2e2e2e,#8a6454)"></div>
  <h2>Catch the season's best recommendations, trial packs, offers, and personalized advice</h2>
  <span class="btn">Login Now</span>
</section>

<!-- feature tiles -->
<div class="tile" style="left:80px">
  <div class="photo" role="img" aria-label="Assorted beauty brand products" style="inset:0;background:linear-gradient(135deg,#6f6f7a,#b3a9a0)"></div>
  <div class="tile-label" style="left:24px;top:22px">Our top 10 brands</div>
  <div class="dark-btn">VIEW ALL BRANDS »</div>
</div>
<div class="tile" style="left:444px">
  <div class="photo" role="img" aria-label="Woman with flowing hair" style="left:120px;top:0;width:192px;height:280px;background:linear-gradient(135deg,#7b4f3b,#c9a084)"></div>
  <div class="photo" style="left:0;top:0;width:130px;height:280px;background:#f3f3f3"></div>
  <div class="tile-label" style="left:16px;top:96px;color:var(--ink);font-family:'Open Sans',Arial,sans-serif;font-size:20px;text-transform:none;line-height:1.4">Natural<br><b style="font-size:24px">BEAUTY<br>SECRETS</b></div>
</div>
<div class="tile" style="left:808px">
  <div class="photo" role="img" aria-label="Makeup artist applying eye makeup" style="inset:0;background:linear-gradient(135deg,#d9c3b5,#8e6b5d)"></div>
  <div class="abs" style="left:0;bottom:0;width:312px;height:72px;background:rgba(34,34,34,.7)"></div>
  <div class="tile-label" style="left:0;bottom:16px;width:312px;text-align:center;font-size:34px">Ask the expert</div>
</div>

<!-- recipe banner -->
<section class="recipe">
  <div class="photo" role="img" aria-label="Smiling woman with aloe vera leaves" style="left:0;top:0;width:380px;height:208px;background:linear-gradient(90deg,#e7cbb6,#b6d79a)"></div>
  <div class="photo" role="img" aria-label="Natural ingredients, bowls and candles" style="left:880px;top:0;width:320px;height:208px;background:linear-gradient(90deg,#cfe6b8,#efe3cf)"></div>
  <div class="recipe-card">
    <h2>Submit your natural<br>beauty recipe</h2>
    <span class="btn">Submit »</span>
  </div>
</section>

<!-- play and quiz panels -->
<section class="panel" style="left:0;width:592px">
  <h2 style="left:76px;top:34px;width:500px">Play the natural beauty game</h2>
  <p style="left:76px;top:120px;width:250px">Lorem Ipsum is simply dummy text of the printing and typesetting industry. Lorem Ipsum has been the industry's standard.</p>
  <div class="abs cond" style="left:76px;top:226px;font-size:24px;color:var(--green-dark)">Sign up today for free</div>
  <span class="btn" style="left:76px;top:282px;width:110px;height:42px;font-size:17px">Play »</span>
  <div class="photo" role="img" aria-label="Red glossy lips" style="left:370px;top:130px;width:170px;height:170px;border-radius:50%;background:radial-gradient(circle,#d6313a,#7a1418);border:6px solid #fff"></div>
</section>
<section class="panel" style="left:608px;width:592px">
  <h2 style="left:44px;top:34px;width:520px">Answer three questions and get a special discount code</h2>
  <div class="abs" style="left:44px;top:146px;font-size:16px;font-weight:700;color:var(--ink)">Question</div>
  <p style="left:44px;top:176px;width:300px;font-size:14px">1.) Lorem Ipsum is simply dummy text of the printing and typesetting industry?</p>
  <span class="btn" style="left:44px;top:282px;width:110px;height:42px;font-size:17px">Next »</span>
  <div class="photo" role="img" aria-label="Red special discount code stamp" style="left:400px;top:150px;width:150px;height:150px;border-radius:50%;border:6px solid var(--stamp);background:#fbe5e5"></div>
</section>

<!-- featured products -->
<div class="section-title" style="top:2064px">Naturally Nice</div>
<svg class="title-rule" style="top:2118px" viewBox="0 0 160 12"><line x1="0" y1="6" x2="70" y2="6" stroke="#7cc242" stroke-width="2"/><circle cx="80" cy="6" r="5" fill="#7cc242"/><line x1="90" y1="6" x2="160" y2="6" stroke="#7cc242" stroke-width="2"/></svg>

<div class="card" style="left:88px">
  <div class="img photo" role="img" aria-label="Boxed soap bar" style="background:linear-gradient(135deg,#e7f2d8,#a9cf7c)"></div>
  <div class="name">PRODUCT TITLE</div><div class="stars">★★★★<i>★</i></div><div class="price">$ 50.00</div>
  <div class="actions"><span>☰ Select Option</span><span>♡ Add to Wishlist</span></div>
</div>
<div class="card" style="left:350px">
  <div class="img photo" role="img" aria-label="Open compact powder" style="background:radial-gradient(circle,#e8cfa9,#f4efe7 70%)"></div>
  <div class="name">PRODUCT TITLE</div><div class="stars">★★★★<i>★</i></div><div class="price">$ 50.00</div>
  <div class="actions"><span>☰ Select Option</span><span>♡ Add to Wishlist</span></div>
</div>
<div class="card" style="left:612px">
  <div class="img photo" role="img" aria-label="Red lipstick" style="background:linear-gradient(180deg,#f6f6f6,#c72a33 60%,#222)"></div>
  <div class="name">PRODUCT TITLE</div><div class="stars">★★★★<i>★</i></div><div class="price">$ 50.00</div>
  <div class="actions"><span>☰ Select Option</span><span>♡ Add to Wishlist</span></div>
</div>
<div class="card" style="left:874px">
  <div class="img photo" role="img" aria-label="Pink cream tube" style="background:linear-gradient(180deg,#f7e6e4,#e9b9b3)"></div>
  <div class="name">PRODUCT TITLE</div><div class="stars">★★★★<i>★</i></div><div class="price">$ 50.00</div>
  <div class="actions"><span>☰ Select Option</span><span>♡ Add to Wishlist</span></div>
</div>

<!-- testimonial -->
<section class="testimonial">
  <div class="section-title" style="top:46px;color:var(--green)">Testimonial</div>
  <svg class="title-rule" style="top:100px" viewBox="0 0 160 12"><line x1="0" y1="6" x2="70" y2="6" stroke="#7cc242" stroke-width="2"/><circle cx="80" cy="6" r="5" fill="#7cc242"/><line x1="90" y1="6" x2="160" y2="6" stroke="#7cc242" stroke-width="2"/></svg>
  <svg class="abs" style="left:120px;top:210px" width="20" height="40" viewBox="0 0 20 40"><path d="M18 2L3 20l15 18" fill="none" stroke="#333" stroke-width="3"/></svg>
  <svg class="abs" style="left:1060px;top:210px" width="20" height="40" viewBox="0 0 20 40"><path d="M2 2l15 18L2 38" fill="none" stroke="#333" stroke-width="3"/></svg>
  <p class="quote">Lorem Ipsum is simply dummy text of the printing and typesetting industry. Lorem Ipsum has been the industry's standard dummy text ever since the 1500s, when an unknown printer took a galley.</p>
  <div class="client">Client name</div>
</section>

<!-- footer -->
<footer class="footer">
  <div class="care">
    <svg width="40" height="40" viewBox="0 0 40 40"><circle cx="20" cy="20" r="19" fill="none" stroke="#fff" stroke-width="2"/><path d="M13 11c-2 2-1 7 4 12s10 6 12 4l-3-4-3 1c-2-1-4-3-5-5l1-3z" fill="#fff"/></svg>
    <div>Customer Care 123 456 789<br>Mon - Sat 9AM to 9PM</div>
  </div>
  <div class="news">Get special discounts on your inbox<div class="field">Enter your email id</div></div>
  <div class="connect">Connect With us<div class="social"><span></span><span></span><span></span><span></span><span></span></div></div>
</footer>
<div class="legal">
  <div class="links"><span>Terms and condition</span><span>Privacy policy</span><span>Shipping policy</span><span>Cancellation and return policy</span></div>
  <div class="copy">© Velmorissa - 2015. All Rights Reserved</div>
</div>

</body>
</html>
```